Property Management Company looking for a high-end business card, letterhead and envelope design.

We provide high-end / boutique property management for real estate investors or individuals looking for someone to manage their portfolio. we are looking for a cohesive high-end design for our business cards, letterhead and envelopes.

Target Market(s)

Real Estate Investors

Industry/Entity Type

Real Estate

Requirements
Must have
• business card, letterhead and envelope design - logo attached

```html
<!DOCTYPE html>
<html lang="en">
<head>
<meta charset="utf-8">
<title>Halden Row Property Management — Stationery</title>
<link href="https://fonts.googleapis.com/css2?family=Montserrat:wght@400;600;700&family=Roboto:wght@400;500&display=swap" rel="stylesheet">
<style>
  :root{
    --navy:#124a86;
    --slate:#8e8f93;
    --ink:#4a4a4d;
    --stage:#47484e;
    --paper:#ffffff;
    --band:#e4e4e4;
    --sky:#a9c0d6;
    --sky-deep:#2f5f94;
  }
  *{margin:0;padding:0;box-sizing:border-box}
  html,body{width:1200px;height:1200px;overflow:hidden}
  body{background:var(--paper);font-family:"Roboto",Arial,sans-serif;color:var(--ink);position:relative}
  .stage{position:absolute;left:0;top:0;width:1200px;height:988px;background:var(--stage)}
  .sheet{position:absolute;background:var(--paper);overflow:hidden}

  /* Plain footer band shared by all pieces */
  .footer-band{position:absolute;left:0;right:0;bottom:0;background:var(--band)}
  .footer-band::before{content:"";position:absolute;left:0;right:0;top:0;height:3px;background:var(--sky)}
  .letterhead .footer-band{height:22px}
  .envelope .footer-band{height:16px}
  .card .footer-band{height:10px}
  .card .footer-band::before{height:2px}
  .card-back .footer-band{background:var(--sky-deep)}

  .wordmark{font-family:"Montserrat",sans-serif;font-weight:600;color:var(--navy);line-height:1}
  .wordmark .name{display:block;letter-spacing:.18em;text-transform:uppercase}
  .wordmark .tag{display:block;letter-spacing:.2em;text-transform:uppercase}

  .contact{display:flex;gap:12px;font-family:"Montserrat",sans-serif;font-weight:600}
  .contact ul{list-style:none}
  .contact li{display:flex;align-items:flex-start;gap:4px;white-space:nowrap}
  .contact .web li{color:var(--navy)}
  .contact .tel li{color:var(--slate)}
  .contact svg{flex:none;fill:currentColor}

  /* Letterhead */
  .letterhead{left:110px;top:200px;width:420px;height:594px}
  .letterhead .wordmark{position:absolute;left:50px;top:66px}
  .letterhead .wordmark .name{font-size:17px}
  .letterhead .wordmark .tag{font-size:7.2px;margin-top:4px;letter-spacing:.22em}
  .letterhead .contact{position:absolute;left:236px;top:66px;font-size:6px}
  .letterhead .contact li{margin-bottom:2px}
  .letter-body{position:absolute;left:50px;top:150px;width:300px}
  .letter-body h1{font-family:"Roboto",Arial,sans-serif;font-weight:500;font-size:14px;color:var(--ink);margin-bottom:18px}
  .letter-body p{font-size:6.4px;line-height:11.6px;margin-bottom:11.6px;color:var(--ink)}
  .signature{position:absolute;left:50px;top:452px;width:46px;height:16px;background:linear-gradient(90deg,#d8d8da,#bdbdc1)}
  .signer{position:absolute;left:50px;top:473px;font-size:6.6px}

  /* Envelope */
  .envelope{left:570px;top:200px;width:520px;height:260px}
  .envelope .wordmark{position:absolute;left:40px;top:56px}
  .envelope .wordmark .name{font-size:14px}
  .envelope .wordmark .tag{font-size:6px;margin-top:3px}
  .envelope .contact{position:absolute;left:40px;top:186px;font-size:5.4px}
  .envelope .contact li{margin-bottom:2px}

  /* Business cards */
  .card{top:500px;width:250px;height:142px}
  .card-front{left:570px}
  .card-back{left:840px;background:var(--navy)}
  .card-front .wordmark{position:absolute;left:20px;top:18px}
  .card-front .wordmark .name{font-size:9px}
  .card-front .wordmark .tag{font-size:3.8px;margin-top:2px}
  .person{position:absolute;right:20px;top:44px;text-align:right;font-family:"Montserrat",sans-serif}
  .person .who{font-weight:700;font-size:7.2px;color:var(--navy);letter-spacing:.04em}
  .person .role{font-weight:600;font-size:4.4px;color:var(--slate);letter-spacing:.12em}
  .card-rule{position:absolute;left:20px;right:20px;top:64px;height:2px;background:var(--navy)}
  .card-front .contact{position:absolute;left:20px;top:72px;font-size:4px;gap:8px}
  .card-front .contact li{margin-bottom:1px}
  .card-back .wordmark{position:absolute;left:0;right:0;top:60px;text-align:center;color:var(--paper)}
  .card-back .wordmark .name{font-size:11px}
  .card-back .wordmark .tag{font-size:4.4px;margin-top:2px}

  /* Brand lockup */
  .lockup{position:absolute;left:0;right:0;top:1064px;text-align:center}
  .lockup .name{font-size:50px;letter-spacing:.2em;padding-left:.2em}
  .lockup .tag{font-family:"Montserrat",sans-serif;font-weight:600;font-size:22px;letter-spacing:.2em;margin-top:10px;padding-left:.2em}
</style>
</head>
<body>
  <div class="stage">

    <article class="sheet letterhead">
      <div class="wordmark"><span class="name">Halden Row</span><span class="tag">Property Management</span></div>
      <div class="contact">
        <ul class="web">
          <li><svg width="6" height="6" viewBox="0 0 10 10"><circle cx="5" cy="5" r="4.5"/></svg>www.haldenrow.com</li>
          <li><svg width="6" height="6" viewBox="0 0 10 10"><rect x="0" y="2" width="10" height="6"/></svg>hello@haldenrow.com</li>
        </ul>
        <ul class="tel">
          <li><svg width="6" height="6" viewBox="0 0 10 10"><rect x="2.5" y="0" width="5" height="10" rx="1"/></svg>0123456789</li>
          <li><svg width="6" height="6" viewBox="0 0 10 10"><path d="M2 0h2l1 3-1.5 1a6 6 0 0 0 2.5 2.5L7 5l3 1v2c0 1-1 2-2 2A8 8 0 0 1 0 2c0-1 1-2 2-2z"/></svg>0123456789</li>
          <li><svg width="6" height="6" viewBox="0 0 10 10"><path d="M5 0a3.6 3.6 0 0 1 3.6 3.6C8.6 6.4 5 10 5 10S1.4 6.4 1.4 3.6A3.6 3.6 0 0 1 5 0z"/></svg>48 Quay Road,<br>Millbrook.</li>
        </ul>
      </div>
      <section class="letter-body">
        <h1>Hello, world!</h1>
        <p>A wonderful serenity has taken possession of my entire soul, like these sweet mornings of spring which I enjoy with my whole heart. I am alone, and feel the charm of existence in this spot, which was created for the bliss of souls like mine. I am so happy, my dear friend, so absorbed in the exquisite sense of mere tranquil existence, that I neglect my talents. I should be incapable of drawing a single stroke at the present moment; and yet I feel that I never was a greater artist than now.</p>
        <p>When, while the lovely valley teems with vapour around me, and the meridian sun strikes the upper surface of the impenetrable foliage of my trees, and but a few stray gleams steal into the inner sanctuary, I throw myself down among the tall grass by the trickling stream; and, as I lie close to the earth, a thousand unknown plants are noticed by me: when I hear the buzz of the little world among the stalks, and grow familiar with the countless indescribable forms of the insects and flies, then I feel the presence of the Almighty, who formed us in his own image, and the breath.</p>
        <p>I am alone, and feel the charm of existence in this spot, which was created for the bliss of souls like mine. I am so happy, my dear friend, so absorbed in the exquisite sense of mere tranquil existence, that I should be incapable of drawing a single stroke at the present moment.</p>
      </section>
      <div class="signature" role="img" aria-label="Handwritten signature"></div>
      <p class="signer">Lena Voss, co-founder</p>
      <div class="footer-band" aria-hidden="true"></div>
    </article>

    <article class="sheet envelope">
      <div class="wordmark"><span class="name">Halden Row</span><span class="tag">Property Management</span></div>
      <div class="contact">
        <ul class="web">
          <li><svg width="5" height="5" viewBox="0 0 10 10"><circle cx="5" cy="5" r="4.5"/></svg>www.haldenrow.com</li>
          <li><svg width="5" height="5" viewBox="0 0 10 10"><rect x="0" y="2" width="10" height="6"/></svg>hello@haldenrow.com</li>
        </ul>
        <ul class="tel">
          <li><svg width="5" height="5" viewBox="0 0 10 10"><rect x="2.5" y="0" width="5" height="10" rx="1"/></svg>0123456789</li>
          <li><svg width="5" height="5" viewBox="0 0 10 10"><path d="M2 0h2l1 3-1.5 1a6 6 0 0 0 2.5 2.5L7 5l3 1v2c0 1-1 2-2 2A8 8 0 0 1 0 2c0-1 1-2 2-2z"/></svg>0123456789</li>
          <li><svg width="5" height="5" viewBox="0 0 10 10"><path d="M5 0a3.6 3.6 0 0 1 3.6 3.6C8.6 6.4 5 10 5 10S1.4 6.4 1.4 3.6A3.6 3.6 0 0 1 5 0z"/></svg>48 Quay Road,<br>Millbrook.</li>
        </ul>
      </div>
      <div class="footer-band" aria-hidden="true"></div>
    </article>

    <article class="sheet card card-front">
      <div class="wordmark"><span class="name">Halden Row</span><span class="tag">Property Management</span></div>
      <div class="person"><div class="who">OWEN MARSH</div><div class="role">DESIGNER</div></div>
      <div class="card-rule"></div>
      <div class="contact">
        <ul class="web">
          <li><svg width="4" height="4" viewBox="0 0 10 10"><circle cx="5" cy="5" r="4.5"/></svg>www.haldenrow.com</li>
          <li><svg width="4" height="4" viewBox="0 0 10 10"><rect x="0" y="2" width="10" height="6"/></svg>hello@haldenrow.com</li>
        </ul>
        <ul class="tel">
          <li><svg width="4" height="4" viewBox="0 0 10 10"><rect x="2.5" y="0" width="5" height="10" rx="1"/></svg>0123456789</li>
          <li><svg width="4" height="4" viewBox="0 0 10 10"><path d="M2 0h2l1 3-1.5 1a6 6 0 0 0 2.5 2.5L7 5l3 1v2c0 1-1 2-2 2A8 8 0 0 1 0 2c0-1 1-2 2-2z"/></svg>0123456789</li>
          <li><svg width="4" height="4" viewBox="0 0 10 10"><path d="M5 0a3.6 3.6 0 0 1 3.6 3.6C8.6 6.4 5 10 5 10S1.4 6.4 1.4 3.6A3.6 3.6 0 0 1 5 0z"/></svg>48 Quay Road,<br>Millbrook.</li>
        </ul>
      </div>
      <div class="footer-band" aria-hidden="true"></div>
    </article>

    <article class="sheet card card-back">
      <div class="wordmark"><span class="name">Halden Row</span><span class="tag">Property Management</span></div>
      <div class="footer-band" aria-hidden="true"></div>
    </article>

  </div>

  <div class="wordmark lockup"><span class="name">Halden Row</span><span class="tag">Property Management</span></div>
</body>
</html>
```